Coastal Meridian Freightworks - needs a website

Build a simple but professional website for Coastal Meridian Freightworks.
Web address is www.cstmerfrt.com.au
We have just completed developing a brochure and the contents of the brochure would serve as the web pages.
Web design does not need to deviate far from the brochure and will not include electronic commerce etc at this stage.

Target Market(s)

Privately owned logistics businesses in Australia

Requirements
Must have
• Professional, elegant, ability to upload video in the future, ability to add e-commerce in the future

```html
<!DOCTYPE html>
<html lang="en">
<head>
<meta charset="utf-8">
<title>Coastal Meridian Freightworks</title>
<link rel="stylesheet" href="https://fonts.googleapis.com/css2?family=Roboto:wght@300;400;500;700;900&display=swap">
<style>
:root{
  --blue:#1b5ba7;
  --blue-dark:#0b3c7c;
  --blue-bright:#1d8fd0;
  --navy:#082f66;
  --grey-btn:#6f808f;
  --card:#6f7e8b;
  --text:#6d6d6d;
  --light:#f1f2f4;
  --white:#ffffff;
}
*{margin:0;padding:0;box-sizing:border-box}
html,body{width:1200px;height:2956px;overflow:hidden;background:var(--white)}
body{font-family:"Roboto",Arial,sans-serif;color:var(--text);position:relative}
.abs{position:absolute}
section,header,nav,footer{position:absolute;left:0;width:1200px;overflow:hidden}
.title{font-weight:700;font-size:23px;letter-spacing:.5px;color:var(--blue);text-transform:uppercase;text-align:center}
.lead{font-size:13.5px;line-height:25px;text-align:center;font-weight:300}
.btn{display:inline-block;background:var(--grey-btn);color:var(--white);font-size:13px;font-weight:500;text-transform:uppercase;padding:0 18px;height:36px;line-height:36px;border-radius:2px}

/* header */
.site-header{top:0;height:108px;background:var(--white)}
.brand{left:75px;top:30px;display:flex;align-items:center;gap:12px}
.brand-square{width:44px;height:44px;background:var(--blue)}
.brand-name{font-size:17px;font-weight:700;color:var(--blue);text-transform:uppercase;line-height:21px;width:200px}
.phone{left:756px;top:44px;font-size:19px;color:var(--blue-dark);font-weight:500;display:flex;align-items:center;gap:8px}
.search{left:915px;top:36px;width:211px;height:36px;background:#f0f1f3;border:1px solid #e1e3e6;font-size:13px;color:#8a8a8a;padding:0 14px;line-height:34px}
.search svg{position:absolute;right:10px;top:9px}

.main-nav{top:108px;height:44px;background:linear-gradient(#2568b7,#144f98)}
.main-nav ul{list-style:none;display:flex;margin-left:75px;height:44px}
.main-nav li{color:var(--white);font-size:13px;font-weight:700;text-transform:uppercase;padding:0 17px;line-height:44px}
.main-nav li.active{background:#8fa3b8}

/* hero */
.hero{top:152px;height:455px}
.hero-photo{width:100%;height:100%;background:linear-gradient(120deg,#3c3f3f 0%,#7b7764 30%,#b6ae95 55%,#8d8978 75%,#d3cfc0 100%)}
.hero-title{left:96px;top:148px;font-size:33px;font-weight:700;color:var(--white);line-height:38px;background:rgba(40,40,40,.45);padding:4px 8px}
.dots{left:1044px;top:410px;display:flex;gap:8px}
.dots span{width:13px;height:13px;border-radius:50%;background:var(--white)}
.dots span:first-child{background:#b9c2cb}

/* welcome */
.welcome{top:607px;height:272px}
.welcome .title{position:absolute;top:40px;width:100%}
.welcome .lead{position:absolute;left:85px;top:86px;width:1030px}
.welcome .btn{position:absolute;left:541px;top:192px}

/* video */
.video{top:879px;height:327px}
.video-photo{width:100%;height:100%;background:linear-gradient(90deg,#2b2a2a,#4a3431 30%,#3d3e44 60%,#2a2b2f)}
.video .title{position:absolute;top:42px;width:100%;color:var(--white)}
.video .lead{position:absolute;left:85px;top:84px;width:1030px;color:#e2e2e2}
.play{left:573px;top:152px}
.video .btn{position:absolute;left:541px;top:240px;background:#7d8b97}

/* solutions */
.solutions{top:1206px;height:430px}
.solutions .title{position:absolute;top:40px;width:100%}
.solutions .lead{position:absolute;top:86px;width:100%}
.solution{top:138px;width:330px;text-align:center}
.solution-icon{width:124px;height:124px;border-radius:50%;margin:0 auto;background:radial-gradient(circle at 50% 30%,#b6c2cd,#7d8d9b 70%);border:4px solid #dfe4e9;display:flex;align-items:center;justify-content:center}
.solution h3{margin-top:26px;font-size:17px;font-weight:700;color:var(--blue);text-transform:uppercase}
.solution p{font-size:13px;line-height:21px;font-weight:300;margin-top:4px;padding:0 22px}

/* company band */
.company{top:1636px;height:256px}
.company-photo{width:100%;height:100%;background:linear-gradient(100deg,#0a2d66 0%,#123f86 40%,#1c5fb0 70%,#0c3675 100%)}
.company .title{position:absolute;top:50px;width:100%;color:var(--white)}
.company .lead{position:absolute;left:85px;top:92px;width:1030px;color:#dfe6f0}
.company .btn{position:absolute;left:541px;top:162px;background:#7a8a99}

/* team */
.team{top:1892px;height:556px}
.team .title{position:absolute;top:40px;width:100%}
.team .lead{position:absolute;top:86px;width:100%}
.member{top:220px;width:330px;height:292px;background:var(--card);text-align:center;color:var(--white)}
.member-photo{top:144px;width:162px;height:162px;border-radius:50%;border:5px solid var(--white);background:linear-gradient(#a7c6dc,#3d5570)}
.member h3{margin-top:104px;font-size:16px;font-weight:700;text-transform:uppercase}
.member .creds{font-size:11px;margin-top:4px}
.member p{font-size:13px;line-height:19px;color:#d7dde2;margin-top:18px;padding:0 30px;font-weight:300}
.social-row{display:flex;gap:14px;justify-content:center;margin-top:20px}
.social-row span{width:15px;height:15px;border-radius:50%;background:#d7dde2}

/* news */
.news{top:2448px;height:281px;background:var(--light)}
.news h2{position:absolute;left:75px;top:36px;font-size:23px;font-weight:700;color:var(--blue);text-transform:uppercase}
.arrows{left:1073px;top:40px;display:flex;gap:8px}
.arrows span{width:21px;height:21px;border-radius:50%;background:#777;display:flex;align-items:center;justify-content:center}
.news-img{width:173px;height:131px;border:4px solid var(--white);background:linear-gradient(#b89d6e,#6d5f4c)}
.news-item{top:90px;width:320px}
.news-item h3{font-size:16px;font-weight:700;font-style:italic;color:var(--blue)}
.news-item .date{font-size:11.5px;margin-top:8px}
.news-item p{font-size:13px;line-height:21px;margin-top:6px;font-weight:300}
.news-item .more{font-size:12px;font-weight:700;color:var(--blue);margin-top:8px;text-transform:uppercase}

/* footer */
.site-footer{top:2729px;height:227px}
.footer-brand{left:75px;top:98px;font-size:15px;font-weight:700;color:var(--white);text-transform:uppercase;display:flex;align-items:center;gap:10px}
.footer-brand span{width:34px;height:34px;background:var(--white)}
.copyright{left:75px;top:185px;font-size:12px;color:#d8e6f4;line-height:17px}
.footer-site h4{font-size:16px;font-weight:700;color:var(--white);text-transform:uppercase}
.footer-links{display:grid;grid-template-columns:130px 100px;row-gap:10px;margin-top:16px;font-size:11px;color:var(--white);text-transform:uppercase}
.contact-list{margin-top:14px;font-size:14px;color:var(--white);line-height:28px}
.contact-list div{display:flex;align-items:center;gap:14px}
.connect{display:flex;gap:16px;margin-top:20px}
.connect span{width:17px;height:17px;border-radius:50%;background:var(--white)}
</style>
</head>
<body>

<header class="site-header">
  <div class="abs brand"><div class="brand-square"></div><div class="brand-name">Coastal Meridian Freightworks</div></div>
  <div class="abs phone">
    <svg width="16" height="16" viewBox="0 0 24 24"><path fill="#0b3c7c" d="M6.6 10.8a15 15 0 0 0 6.6 6.6l2.2-2.2c.3-.3.7-.4 1-.2 1.1.4 2.3.6 3.6.6.6 0 1 .4 1 1V20c0 .6-.4 1-1 1A17 17 0 0 1 3 4c0-.6.4-1 1-1h3.5c.6 0 1 .4 1 1 0 1.3.2 2.5.6 3.6.1.3 0 .7-.2 1z"/></svg>
    07 3555 0148
  </div>
  <div class="abs search">Search...
    <svg width="17" height="17" viewBox="0 0 24 24"><circle cx="10" cy="10" r="7" fill="none" stroke="#1b5ba7" stroke-width="3"/><path d="M15 15l6 6" stroke="#1b5ba7" stroke-width="3"/></svg>
  </div>
</header>

<nav class="main-nav">
  <ul>
    <li class="active">Home</li><li>Who We Are</li><li>What We Do</li><li>Our Solutions</li><li>Latest News</li><li>Benefits</li><li>Blog</li><li>Careers</li><li>Contact</li>
  </ul>
</nav>

<section class="hero">
  <div class="hero-photo" role="img" aria-label="Warehouse interior with tall pallet racking and two forklifts"></div>
  <h1 class="abs hero-title">A New Solution For Australia Warehouse<br>Business Owners..</h1>
  <svg class="abs" style="left:0;top:300px" width="1200" height="155" viewBox="0 0 1200 155">
    <path d="M0 155 C300 90 700 60 1200 90 L1200 155Z" fill="#1a5fae"/>
    <path d="M0 155 C350 110 750 95 1200 125 L1200 155Z" fill="#ffffff"/>
  </svg>
  <div class="abs dots"><span></span><span></span><span></span><span></span></div>
</section>

<section class="welcome">
  <h2 class="title">Welcome To Our Company Website</h2>
  <p class="lead">Aliquam molestie, mi et imperdiet euismod, dui purus auctor tellus, et interdum lacus lectus et ante. Sed accumsan sollicitudin sapien, sit amet adipiscing turpis gravida ac. In congue, neque ac lobortis volutpat, libero mauris varius mi, vitae suscipit ipsum ligula vitae risus. Duis aliquam nibh a dui iaculis viverra id a velit. Vivamus egestas risus in magna varius commodo. Sed semper viverra egestas. Etiam pretium porttitor lectus, vel ornare neque porta volutpat.</p>
  <span class="btn">Read More</span>
  <svg class="abs" style="left:960px;top:120px" width="240" height="152" viewBox="0 0 240 152">
    <path d="M20 152 C80 100 160 40 240 20 L240 152Z" fill="#8a96a2"/>
    <path d="M60 152 C120 90 180 40 240 0 L240 152Z" fill="#1d8fd0"/>
  </svg>
</section>

<section class="video">
  <div class="video-photo" role="img" aria-label="Dimly lit warehouse aisle with pallet racking"></div>
  <h2 class="title">Watch A Video What We Do</h2>
  <p class="lead">Aliquam molestie, mi et imperdiet euismod, dui purus auctor tellus, et interdum lacus lectus et ante. Sed accumsan sollicitudin sapien, sit amet adipiscing turpis gravida ac. In congue, neque ac lobortis volutpat, libero mauris varius mi, vitae suscipit ipsum ligula vitae risus.</p>
  <svg class="abs play" width="54" height="54" viewBox="0 0 54 54"><circle cx="27" cy="27" r="24" fill="none" stroke="#8fa3b6" stroke-width="5"/><path d="M21 16 L38 27 L21 38Z" fill="#8fa3b6"/></svg>
  <span class="btn">Watch Video</span>
</section>

<section class="solutions">
  <svg class="abs" style="left:0;top:0" width="220" height="180" viewBox="0 0 220 180">
    <path d="M0 180 C60 150 130 80 190 0 L0 0Z" fill="#1d8fd0"/>
    <path d="M160 0 C130 40 100 60 60 80 C110 60 150 30 200 0Z" fill="#8a96a2"/>
  </svg>
  <h2 class="title">Our Solutions</h2>
  <p class="lead">Duis aliquam nibh a dui iaculis viverra id a velit. Vivamus egestas risus in magna varius commodo. Sed semper viverra egestas.</p>

  <div class="abs solution" style="left:75px">
    <div class="solution-icon"><svg width="54" height="44" viewBox="0 0 54 44"><path d="M4 2 V40 H52" fill="none" stroke="#fff" stroke-width="3"/><rect x="12" y="26" width="7" height="12" fill="#fff"/><rect x="23" y="20" width="7" height="18" fill="#fff"/><rect x="34" y="14" width="7" height="24" fill="#fff"/><path d="M10 22 L24 12 L32 16 L48 4" fill="none" stroke="#fff" stroke-width="3"/></svg></div>
    <h3>Scale</h3>
    <p>Duis aliquam nibh a dui iaculis viverra id a velit. Vivamus egestas risus in magna varius commodo. Sed semper viverra egestas...</p>
  </div>
  <div class="abs solution" style="left:435px">
    <div class="solution-icon"><svg width="56" height="44" viewBox="0 0 56 44"><circle cx="28" cy="10" r="6" fill="#fff"/><circle cx="10" cy="26" r="5" fill="#fff"/><circle cx="46" cy="26" r="5" fill="#fff"/><path d="M18 24 a10 8 0 0 1 20 0Z" fill="#fff"/><path d="M2 42 a8 7 0 0 1 16 0Z M38 42 a8 7 0 0 1 16 0Z" fill="#fff"/><path d="M14 10 a14 14 0 0 1 8-6 M42 10 a14 14 0 0 0-8-6" stroke="#fff" stroke-width="2" fill="none"/></svg></div>
    <h3>Synergy</h3>
    <p>Duis aliquam nibh a dui iaculis viverra id a velit. Vivamus egestas risus in magna varius commodo. Sed semper viverra egestas...</p>
  </div>
  <div class="abs solution" style="left:795px">
    <div class="solution-icon"><svg width="50" height="50" viewBox="0 0 50 50"><circle cx="14" cy="10" r="6" fill="#fff"/><rect x="8" y="18" width="12" height="18" fill="#fff"/><rect x="8" y="36" width="5" height="12" fill="#fff"/><rect x="15" y="36" width="5" height="12" fill="#fff"/><rect x="26" y="22" width="20" height="26" fill="#fff"/></svg></div>
    <h3>Value</h3>
    <p>Duis aliquam nibh a dui iaculis viverra id a velit. Vivamus egestas risus in magna varius commodo. Sed semper viverra egestas...</p>
  </div>
</section>

<section class="company">
  <div class="company-photo" role="img" aria-label="Blue toned background of interlocking puzzle pieces"></div>
  <h2 class="title">Coastal Meridian Freightworks Company</h2>
  <p class="lead">Aliquam molestie, mi et imperdiet euismod, dui purus auctor tellus, et interdum lacus lectus et ante. Sed accumsan sollicitudin sapien, sit amet adipiscing turpis gravida ac. In congue, neque ac lobortis volutpat, libero mauris varius mi, vitae suscipit ipsum ligula vitae risus.</p>
  <span class="btn">Read More</span>
</section>

<section class="team">
  <svg class="abs" style="left:860px;top:0" width="340" height="200" viewBox="0 0 340 200">
    <path d="M0 0 C40 20 90 10 130 0Z" fill="#8a96a2"/>
    <path d="M120 0 C180 60 260 150 340 190 L340 0Z" fill="#1d8fd0"/>
  </svg>
  <h2 class="title">Our Team</h2>
  <p class="lead">Duis aliquam nibh a dui iaculis viverra id a velit. Vivamus egestas risus in magna varius commodo. Sed semper viverra egestas.</p>

  <div class="abs member" style="left:75px">
    <h3>Daniel Marsh</h3><div class="creds">BCom, FAICD, CPA, FACILT</div>
    <p>Sed accumsan sollicitudin sapien, sit amet adipiscing turpis gravida ac. In congue, neque ac lobortis volutpat, libero mauris...</p>
    <div class="social-row"><span></span><span></span><span></span></div>
  </div>
  <div class="abs member-photo" style="left:159px" role="img" aria-label="Portrait of team member"></div>

  <div class="abs member" style="left:435px">
    <h3>Daniel Marsh</h3><div class="creds">BCom, FAICD, CPA, FACILT</div>
    <p>Sed accumsan sollicitudin sapien, sit amet adipiscing turpis gravida ac. In congue, neque ac lobortis volutpat, libero mauris...</p>
    <div class="social-row"><span></span><span></span><span></span></div>
  </div>
  <div class="abs member-photo" style="left:519px" role="img" aria-label="Portrait of team member"></div>

  <div class="abs member" style="left:795px">
    <h3>Daniel Marsh</h3><div class="creds">BCom, FAICD, CPA, FACILT</div>
    <p>Sed accumsan sollicitudin sapien, sit amet adipiscing turpis gravida ac. In congue, neque ac lobortis volutpat, libero mauris...</p>
    <div class="social-row"><span></span><span></span><span></span></div>
  </div>
  <div class="abs member-photo" style="left:879px" role="img" aria-label="Portrait of team member"></div>
</section>

<section class="news">
  <h2>Latest News</h2>
  <div class="abs arrows">
    <span><svg width="9" height="9" viewBox="0 0 10 10"><path d="M7 1 L3 5 L7 9" stroke="#fff" stroke-width="2" fill="none"/></svg></span>
    <span><svg width="9" height="9" viewBox="0 0 10 10"><path d="M3 1 L7 5 L3 9" stroke="#fff" stroke-width="2" fill="none"/></svg></span>
  </div>
  <div class="abs news-img" style="left:75px;top:94px" role="img" aria-label="Warehouse aisle with stocked shelving"></div>
  <div class="abs news-item" style="left:270px">
    <h3>Aliquam ullamcorper tempor felis..</h3>
    <div class="date">Posted Nov 25, 2015</div>
    <p>Duis aliquam nibh a dui iaculis viverra id a velit. Vivamus egestas risus in magna varius commodo.</p>
    <div class="more">Learn More</div>
  </div>
  <div class="abs news-img" style="left:617px;top:94px;background:linear-gradient(#3f68a8,#b27a4a)" role="img" aria-label="Blue pallet racking loaded with goods"></div>
  <div class="abs news-item" style="left:808px">
    <h3>Aliquam ullamcorper tempor felis..</h3>
    <div class="date">Posted Nov 25, 2015</div>
    <p>Duis aliquam nibh a dui iaculis viverra id a velit. Vivamus egestas risus in magna varius commodo.</p>
    <div class="more">Learn More</div>
  </div>
</section>

<footer class="site-footer">
  <svg class="abs" style="left:0;top:0" width="1200" height="227" viewBox="0 0 1200 227">
    <defs><linearGradient id="footerBlue" x1="0" y1="0" x2="1" y2="0"><stop offset="0" stop-color="#0b3c7c"/><stop offset="0.6" stop-color="#1660b0"/><stop offset="1" stop-color="#1d8fd0"/></linearGradient></defs>
    <rect width="1200" height="227" fill="#f1f2f4"/>
    <path d="M0 30 C300 10 500 40 700 50 C900 60 1050 40 1200 0 L1200 227 L0 227Z" fill="#7d8b98"/>
    <path d="M0 70 C300 20 600 40 800 50 C1000 60 1100 40 1200 20 L1200 227 L0 227Z" fill="url(#footerBlue)"/>
  </svg>
  <div class="abs footer-brand"><span></span>Coastal Meridian<br>Freightworks</div>
  <div class="abs copyright">Copyright © 2015. Company Name<br>All Right Reserved</div>

  <div class="abs footer-site" style="left:433px;top:58px">
    <h4>Company</h4>
    <div class="footer-links">
      <span>Home</span><span>Benefits</span><span>Who We Are</span><span>Blog</span><span>What We Do</span><span>Careers</span><span>Our Solutions</span><span>Contact</span><span>Latest News</span>
    </div>
  </div>

  <div class="abs footer-site" style="left:713px;top:58px">
    <h4>Contact Us</h4>
    <div class="contact-list">
      <div><svg width="13" height="13" viewBox="0 0 24 24"><path fill="#fff" d="M6.6 10.8a15 15 0 0 0 6.6 6.6l2.2-2.2c.3-.3.7-.4 1-.2 1.1.4 2.3.6 3.6.6.6 0 1 .4 1 1V20c0 .6-.4 1-1 1A17 17 0 0 1 3 4c0-.6.4-1 1-1h3.5c.6 0 1 .4 1 1 0 1.3.2 2.5.6 3.6.1.3 0 .7-.2 1z"/></svg>07 3555 0148</div>
      <div><svg width="13" height="13" viewBox="0 0 24 24"><rect x="6" y="1" width="12" height="22" rx="2" fill="none" stroke="#fff" stroke-width="2.5"/></svg>0400 555 217</div>
      <div><svg width="13" height="13" viewBox="0 0 24 24"><rect x="1" y="4" width="22" height="16" fill="#fff"/><path d="M1 4 L12 13 L23 4" stroke="#1660b0" stroke-width="2" fill="none"/></svg>info@cstmerfrt.com.au</div>
    </div>
  </div>

  <div class="abs footer-site" style="left:952px;top:58px">
    <h4>Connect Us</h4>
    <div class="connect"><span></span><span></span><span></span><span></span><span></span></div>
  </div>
</footer>

</body>
</html>
```